Vara - Boutique Lawfirm providing legal advice to regulated financial institutions

I'm looking for a web page for my boutique law firm, specialized in providing legal advice to financial regulated institutions as well as non-financial regulated entities. The web page should have the technical capability to be in Spanish and English. Logo, color and typography according to specs provided. The web page should at least have the following (titles names may vary): 1. Homepage that communicates quickly and succinctly exactly what the law firm specializes in, grabs attention with eye-catching images and immediately establishes credibility 2. Our Firm; 3. Practice Area, 4. Resource Center, 5. Contact us, 6. Case Study. 7. Social Responsibility. The web page should also: -have the capability to add videos. -be owned and edited by our company. -be amicable with Instagram and LinkedIn. -SEO -adaptable to mobile version. PLEASE SEE WEB SITE REFERENCE IN NICE TO HAVE SECTION

Target Market(s)

Banks, financial institutions, lawyers

Industry/Entity Type

Financial

Coding

Coded - Design and coding required

Number of Pages Required

5+ page

Font styles to use
Serif

Requirements
Must have
• Contact Form
Social media links (Instagram and Linkedin)
Nice to have
• Link to Whatsapp number

see these web sites for
references
https://www.briefmarkt.com
https://www.quillnest.com
https://www.pemberdale.com/en/capabilities/services/financial-services/consulting

```html
<!DOCTYPE html>
<html lang="en">
<head>
<meta charset="utf-8">
<title>Vara – Legal Services</title>
<link href="https://fonts.googleapis.com/css2?family=Roboto:wght@400;500;700;900&family=Montserrat:wght@300;400;500;600;700&family=Open+Sans:wght@400;600&display=swap" rel="stylesheet">
<style>
:root{
  --green:#2f8c63;
  --green-dark:#226b4b;
  --green-light:#3aa574;
  --navy:#1f3046;
  --navy-deep:#16263a;
  --footer:#101b2a;
  --ink:#1a2533;
  --muted:#5d6570;
  --white:#ffffff;
  --light:#eef5f3;
}
*{margin:0;padding:0;box-sizing:border-box}
html,body{width:1200px;height:4478px;overflow:hidden}
body{font-family:"Open Sans",sans-serif;color:var(--ink);background:var(--white);position:relative}
section,header,footer{position:relative;width:1200px;overflow:hidden}
.abs{position:absolute}
.btn{position:absolute;display:flex;align-items:center;justify-content:center;font-family:"Montserrat",sans-serif;font-weight:700;font-size:14px;letter-spacing:.5px;color:var(--white);text-decoration:none;border-radius:2px}

/* hero */
.hero{height:748px}
.hero-photo{position:absolute;inset:0;background:linear-gradient(100deg,#173c33 0%,#2a8a62 28%,#6fb597 46%,#c9ddd6 62%,#e6efec 100%)}
.nav{position:absolute;top:0;left:0;width:1200px;height:120px}
.logo{position:absolute;font-family:"Montserrat",sans-serif;color:var(--white)}
.logo .word{font-weight:400;letter-spacing:1px;line-height:1}
.logo .tag{font-weight:400;letter-spacing:8px;text-transform:uppercase;line-height:1}
.nav .logo{left:92px;top:30px}
.nav .logo .word{font-size:52px}
.nav .logo .tag{font-size:10px;letter-spacing:6px;margin-top:2px}
.menu{position:absolute;top:52px;left:367px;display:flex;gap:26px;font-family:"Montserrat",sans-serif;font-size:15px;font-weight:500;color:var(--ink)}
.menu a{color:var(--ink);text-decoration:none}
.menu a.active{text-decoration:underline}
.lang{position:absolute;left:1016px;top:44px;width:90px;height:36px;border:2px solid #5a6470;border-radius:3px;font-family:"Montserrat",sans-serif;font-size:14px;display:flex;align-items:center;justify-content:center;gap:10px}
.hero-brand{left:720px;top:248px;color:var(--green)}
.hero-brand .word{font-size:96px;color:var(--green);font-weight:500;line-height:96px}
.hero-brand .tag{font-size:19px;letter-spacing:18px;color:var(--green);margin-top:6px}
.hero-text{left:722px;top:392px;width:390px;font-family:"Montserrat",sans-serif;font-size:16px;line-height:26px;color:#1f2a33}
.hero .btn{left:722px;top:498px;width:167px;height:46px;background:var(--green);box-shadow:0 3px 6px rgba(0,0,0,.25)}
.dots{position:absolute;top:688px;left:568px;display:flex;gap:8px}
.dots span{width:16px;height:16px;border-radius:50%;border:2px solid var(--white)}
.dots span.on{background:var(--white)}

/* services */
.services{height:261px;margin-top:7px;display:flex;gap:6px;background:var(--white)}
.service{flex:1;background:var(--navy);color:var(--white);text-align:center;padding-top:40px;position:relative}
.service.featured{background:var(--green)}
.service.featured::after{content:"";position:absolute;left:50%;bottom:-12px;margin-left:-12px;border:12px solid transparent;border-bottom:0;border-top-color:var(--green)}
.service h3{font-family:"Montserrat",sans-serif;font-size:17px;font-weight:600;margin-top:14px;text-transform:uppercase}
.service p{font-family:"Montserrat",sans-serif;font-size:12.5px;line-height:20px;width:320px;margin:18px auto 0}

/* firm */
.firm{height:565px}
.firm-art{left:148px;top:100px;width:380px;height:380px;border-radius:50%;background:radial-gradient(circle,#ffffff 0%,#ffffff 22%,#4b9a74 40%,#2b4f47 65%,#ffffff 72%)}
.firm h2{position:absolute;left:594px;top:132px;font-family:"Roboto",sans-serif;font-weight:700;font-size:32px;color:var(--navy)}
.firm p{position:absolute;left:594px;top:195px;width:465px;font-family:"Roboto",sans-serif;font-size:14px;line-height:26px;color:var(--muted)}
.firm .btn{left:594px;top:422px;width:175px;height:50px;background:linear-gradient(90deg,var(--navy),#1f4a47)}

/* stats */
.stats{height:202px;background:var(--green);display:flex;justify-content:center;align-items:center}
.stat{width:236px;text-align:center;color:var(--white);position:relative}
.stat + .stat::before{content:"";position:absolute;left:0;top:-6px;height:122px;border-left:1px solid rgba(255,255,255,.5)}
.stat b{display:block;font-family:"Roboto",sans-serif;font-size:27px;font-weight:700;margin-top:12px}
.stat span{display:block;font-family:"Montserrat",sans-serif;font-size:15px;font-weight:500;margin-top:4px}

/* practice */
.practice{height:829px;background:linear-gradient(180deg,#2a3a50 0%,#23344a 50%,#1f3046 100%)}
.practice-photo{position:absolute;inset:0;background:linear-gradient(90deg,rgba(60,75,95,.6),rgba(30,45,65,.2) 50%,rgba(60,75,95,.55))}
.title-box{position:absolute;font-family:"Roboto",sans-serif;font-weight:700;text-align:center}
.title-box .frame{position:absolute}
.practice .title-box{left:420px;top:90px;width:360px;font-size:37px;color:var(--white)}
.practice .title-box .frame{left:173px;top:-6px;width:165px;height:82px;border:2px solid var(--white);border-left:none}
.card-frame{position:absolute;border:4px solid var(--green);width:343px;height:470px;top:255px}
.card-img{position:absolute;width:202px;height:354px;top:313px;border:3px solid var(--green)}
.card-img.a{background:linear-gradient(160deg,#7d5a3c,#3c3c45 55%,#c8c8c8)}
.card-img.b{background:linear-gradient(160deg,#c9ccd1,#2f3d56 55%,#b8b3aa)}
.card-text{position:absolute;top:325px;width:200px;color:var(--white)}
.card-text h3{font-family:"Roboto",sans-serif;font-weight:700;font-size:25px;line-height:35px;text-transform:uppercase}
.card-text p{font-family:"Roboto",sans-serif;font-weight:500;font-size:12.5px;line-height:25px;margin-top:18px}
.card-text a{display:flex;align-items:center;justify-content:center;width:128px;height:50px;border:2px solid var(--white);font-family:"Montserrat",sans-serif;font-size:13px;font-weight:600;color:var(--white);text-decoration:none;margin-top:22px}
.arrow{position:absolute;top:470px}

/* resource */
.resource{height:590px;background:linear-gradient(180deg,#f6fbfa 0%,#e6f2ef 30%,#cdd8e4 45%,#6f88ad 70%,#2f4670 100%)}
.resource-photo{position:absolute;left:0;top:200px;width:1200px;height:390px;background:linear-gradient(180deg,rgba(150,170,200,.3),rgba(40,60,100,.7))}
.resource h2{position:absolute;left:144px;top:55px;font-family:"Roboto",sans-serif;font-weight:900;font-size:44px;line-height:54px;color:var(--ink)}
.resource p{position:absolute;left:463px;top:60px;width:590px;font-family:"Roboto",sans-serif;font-size:14px;line-height:27px;color:var(--muted)}
.resource .btn{left:461px;top:219px;width:175px;height:50px;background:linear-gradient(90deg,var(--navy),#1f4a47)}

/* news */
.news{height:755px}
.news .title-box{left:440px;top:110px;width:320px;font-size:38px}
.news .title-box .g{color:var(--green)}
.news .title-box .n{color:var(--ink)}
.news .title-box .frame{left:151px;top:-14px;width:144px;height:84px;border:2px solid var(--ink);border-left:none}
.post{position:absolute;top:224px;width:281px;height:418px;background:var(--white);box-shadow:0 6px 14px rgba(47,140,99,.22)}
.post-img{height:226px}
.post-img.a{background:linear-gradient(135deg,#5c4a3c,#c9a27b 60%,#3b3a3a)}
.post-img.b{background:linear-gradient(135deg,#e9eaee,#8da0c0 55%,#344a72)}
.post-img.c{background:linear-gradient(135deg,#33313a,#6c5c55 50%,#1f2330)}
.post h4{font-family:"Montserrat",sans-serif;font-weight:600;font-size:13.5px;line-height:24px;margin:26px 0 0 22px;text-transform:uppercase;color:#222}
.post .date{margin:8px 0 0 22px;font-family:"Montserrat",sans-serif;font-size:13.5px;color:var(--green);display:flex;align-items:center;gap:6px}
.post p{margin:10px 0 0 22px;width:240px;font-family:"Montserrat",sans-serif;font-size:12.5px;line-height:22px;color:var(--muted)}

/* footer */
footer{height:530px;background:var(--footer);color:var(--white)}
footer .logo{left:183px;top:150px}
footer .logo .word{font-size:76px}
footer .logo .tag{font-size:14px;letter-spacing:11px;margin-top:4px}
.social{position:absolute;left:183px;top:267px;display:flex;gap:22px}
.social a{width:40px;height:40px;border-radius:50%;background:var(--green);display:block}
.field{position:absolute;border:2px solid #d8dde3;height:52px;font-family:"Montserrat",sans-serif;font-size:15px;color:#cfd6df;padding:14px 12px}
.submit{position:absolute;left:577px;top:332px;width:133px;height:54px;background:var(--green);border:2px solid #7bc3a1;font-family:"Montserrat",sans-serif;font-size:17px;font-weight:500;color:var(--white);display:flex;align-items:center;justify-content:center}
.rule{position:absolute;left:183px;top:438px;width:912px;border-top:1px solid #3a4657}
.copy{position:absolute;left:0;top:472px;width:1200px;text-align:center;font-family:"Montserrat",sans-serif;font-size:14px;color:#e6e9ee}
</style>
</head>
<body>

<header class="hero">
  <div class="hero-photo" role="img" aria-label="Man in glasses with a green city skyline and stock chart overlay"></div>
  <div class="nav">
    <div class="logo"><div class="word">Vara</div><div class="tag">Legal Services</div></div>
    <nav class="menu">
      <a class="active" href="#">Home</a><a href="#">Our Firm</a><a href="#">Practice Area</a><a href="#">Resource Center</a><a href="#">Case Study</a><a href="#">Contact</a>
    </nav>
    <div class="lang">ENG <svg width="12" height="8" viewBox="0 0 12 8"><path d="M1 1l5 5 5-5" fill="none" stroke="#1a2533" stroke-width="1.6"/></svg></div>
  </div>
  <div class="logo hero-brand abs"><div class="word">Vara</div><div class="tag">Legal Services</div></div>
  <p class="hero-text abs">Sed ut perspiciatis unde omnis iste natus error sit voluptatem accusantium doloremque laudantium, totam rem aperiam, eaque ipsa</p>
  <a class="btn" href="#">LEARN MORE</a>
  <div class="dots"><span class="on"></span><span></span><span></span></div>
</header>

<section class="services">
  <div class="service">
    <svg width="48" height="50" viewBox="0 0 48 50" fill="none" stroke="#fff" stroke-width="2"><rect x="6" y="3" width="28" height="38"/><path d="M12 12h16M12 18h16M12 24h12M12 30h8"/><path d="M30 44l12-18 4 3-12 18z"/></svg>
    <h3>Legal</h3>
    <p>Lorem ipsum dolor amet, consectetur adipiscing elit, sed do eiusmod tempor incididunt ut labore et minim veniam dolore magna aliqua.</p>
  </div>
  <div class="service featured">
    <svg width="52" height="52" viewBox="0 0 52 52" fill="none" stroke="#fff" stroke-width="2"><rect x="8" y="6" width="30" height="40"/><path d="M14 16h18M14 22h18M14 28h12"/><circle cx="38" cy="36" r="9"/><path d="M38 31v10M35 34h5"/></svg>
    <h3>Financial Services</h3>
    <p>Lorem ipsum dolor amet, consectetur adipiscing elit, sed do eiusmod tempor incididunt ut labore et minim veniam dolore magna aliqua.</p>
  </div>
  <div class="service">
    <svg width="50" height="50" viewBox="0 0 50 50" fill="none" stroke="#fff" stroke-width="2"><rect x="6" y="4" width="30" height="40"/><path d="M12 14h18M12 20h18M12 26h10"/><circle cx="37" cy="34" r="8"/><path d="M33 34l3 3 5-6"/></svg>
    <h3>Managed Legal Services</h3>
    <p>Lorem ipsum dolor amet, consectetur adipiscing elit, sed do eiusmod tempor incididunt ut labore et minim veniam dolore magna aliqua.</p>
  </div>
</section>

<section class="firm">
  <div class="firm-art abs" role="img" aria-label="Circular arrangement of green and dark dots forming a ring"></div>
  <h2>OUR FIRM</h2>
  <p>Lorem ipsum dolor sit amet, consectetur adipiscing elit, sed eiusmod tempor incididunt ut labore et dolore magna aliqua. Ut enim ad minim veniam, quis nostrud exercitation ullamco laboris nisi ut aliquip ex commodo consequat. Duis aute irure dolor in reprehenderit in voluptate velit esse cillum dolore eu fugiat nulla pariatur. Excepteur sint occaecat cupidatat non proident, sunt in culpa qui officia deserunt mollit anim id est laborum. reprehenderit in voluptate</p>
  <a class="btn" href="#">LEARN MORE</a>
</section>

<section class="stats">
  <div class="stat">
    <svg width="60" height="44" viewBox="0 0 60 44" fill="#fff"><path d="M2 10l14-6 14 8 14-8 14 6-6 16-22 14-22-14z"/></svg>
    <b>150 +</b><span>Lorem ipsum dolor amet</span>
  </div>
  <div class="stat">
    <svg width="48" height="46" viewBox="0 0 48 46" fill="none" stroke="#fff" stroke-width="3"><rect x="4" y="8" width="40" height="34" rx="2"/><path d="M4 17h40M14 3v10M34 3v10"/><path d="M12 24h6M22 24h6M32 24h6M12 32h6M22 32h6M32 32h6"/></svg>
    <b>150 +</b><span>Lorem ipsum dolor amet</span>
  </div>
  <div class="stat">
    <svg width="48" height="46" viewBox="0 0 48 46" fill="none" stroke="#fff" stroke-width="3"><path d="M12 4h26v30H12z"/><circle cx="25" cy="16" r="5"/><path d="M6 34h30v8H6z"/></svg>
    <b>150 +</b><span>Lorem ipsum dolor amet</span>
  </div>
  <div class="stat">
    <svg width="54" height="48" viewBox="0 0 54 48" fill="none" stroke="#fff" stroke-width="3"><rect x="6" y="6" width="28" height="36" rx="2"/><path d="M14 3h12v6H14zM12 18h16M12 26h10"/><circle cx="40" cy="34" r="10" fill="#fff"/><path d="M35 34l4 4 6-7" stroke="#2f8c63"/></svg>
    <b>150 +</b><span>Lorem ipsum dolor amet</span>
  </div>
</section>

<section class="practice">
  <div class="practice-photo" role="img" aria-label="Law library with shelves of books, dimmed in navy"></div>
  <div class="title-box"><span class="frame"></span>PRACTICE AREA</div>

  <div class="card-frame" style="left:247px"></div>
  <div class="card-img a" style="left:144px" role="img" aria-label="Lawyer in a suit working at a laptop in an office"></div>
  <div class="card-text" style="left:371px">
    <h3>Financial Institutions</h3>
    <p>Nam libero tempore, cum soluta nobis est eligendi optio cumque nihil impedit quo minus id quod placeat facere possimus, omnis libero tempore, cum soluta</p>
    <a href="#">READ MORE</a>
  </div>

  <div class="card-frame" style="left:713px"></div>
  <div class="card-img b" style="left:612px" role="img" aria-label="Lawyer in a navy suit seated at a desk"></div>
  <div class="card-text" style="left:838px">
    <h3>Non-Financial Entities</h3>
    <p>Nam libero tempore, cum soluta nobis est eligendi optio cumque nihil impedit quo minus id quod placeat facere possimus, omnis voluptas as sumenda est. Nam libero tempore, cum soluta</p>
    <a href="#">READ MORE</a>
  </div>

  <svg class="arrow" style="left:38px" width="30" height="56" viewBox="0 0 30 56"><path d="M27 2L3 28l24 26" fill="none" stroke="#fff" stroke-width="3"/></svg>
  <svg class="arrow" style="left:1134px" width="30" height="56" viewBox="0 0 30 56"><path d="M3 2l24 26L3 54" fill="none" stroke="#fff" stroke-width="3"/></svg>
</section>

<section class="resource">
  <div class="resource-photo" role="img" aria-label="Empty boardroom table with laptops and a city skyline through windows"></div>
  <h2>RESOURCE<br>CENTER</h2>
  <p>Lorem ipsum dolor sit amet, consectetur adipiscing elit, sed do eiusmod tempor incididunt ut labore et dolore magna aliquis ipsum suspendisse ultrices gravida.Risus commodo viverra maecenas accumsan lacus vel facilisis.Lorem ipsum dolor sit amet, consectetur adipiscing elit, sed do eiusmod tempor incididunt ut labore et dolore magna aliquuis ipsum suidsus commodiverra maecenas accumsan lacus vel facilisis.</p>
  <a class="btn" href="#">LEARN MORE</a>
</section>

<section class="news">
  <div class="title-box"><span class="frame"></span><span class="g">LATEST</span> <span class="n">NEWS</span></div>
  <article class="post" style="left:136px">
    <div class="post-img a" role="img" aria-label="Man working on a laptop in a cafe"></div>
    <h4>Nemo enim ipsam volup<br>quia voluptas sit</h4>
    <div class="date"><svg width="12" height="12" viewBox="0 0 12 12" fill="#2f8c63"><rect x="0" y="2" width="12" height="10" rx="1"/></svg>FEB 3, 2020</div>
    <p>Sed ut perspiciatis unde omnis iste natus error sit voluptatem acsntium domque laudantium, totam</p>
  </article>
  <article class="post" style="left:456px">
    <div class="post-img b" role="img" aria-label="Hands reviewing financial charts on paper"></div>
    <h4>Nemo enim ipsam volup<br>quia voluptas sit</h4>
    <div class="date"><svg width="12" height="12" viewBox="0 0 12 12" fill="#2f8c63"><rect x="0" y="2" width="12" height="10" rx="1"/></svg>FEB 3, 2020</div>
    <p>Sed ut perspiciatis unde omnis iste natus error sit voluptatem acsntium domque laudantium, totam</p>
  </article>
  <article class="post" style="left:777px">
    <div class="post-img c" role="img" aria-label="Colleagues looking at a laptop together"></div>
    <h4>Nemo enim ipsam volup<br>quia voluptas sit</h4>
    <div class="date"><svg width="12" height="12" viewBox="0 0 12 12" fill="#2f8c63"><rect x="0" y="2" width="12" height="10" rx="1"/></svg>FEB 3, 2020</div>
    <p>Sed ut perspiciatis unde omnis iste natus error sit voluptatem acsntium domque laudantium, totam</p>
  </article>
</section>

<footer>
  <div class="logo"><div class="word">Vara</div><div class="tag">Legal Services</div></div>
  <div class="social">
    <a href="#" aria-label="Social profile 1"></a><a href="#" aria-label="Social profile 2"></a><a href="#" aria-label="Social profile 3"></a><a href="#" aria-label="Social profile 4"></a><a href="#" aria-label="Social profile 5"></a>
  </div>
  <div class="field" style="left:577px;top:92px;width:254px">Surname</div>
  <div class="field" style="left:841px;top:92px;width:254px">First name</div>
  <div class="field" style="left:577px;top:158px;width:254px">Phone</div>
  <div class="field" style="left:841px;top:158px;width:254px">Email</div>
  <div class="field" style="left:577px;top:222px;width:518px;height:96px">Your message</div>
  <div class="submit">SUBMIT</div>
  <div class="rule"></div>
  <div class="copy">Copyrights @ 2020 Vara. All Rights Reserved.</div>
</footer>

</body>
</html>
```